Website Creation for Auto Repair Marketing Company - Torque Lane Promotions

This will be a website and logo for a digital marketing agency servicing the auto repair industry.

Focus on modern, efficient, and easy to understand navigation and flow. We want users to easily sign up for our Review Software and a Visibility Audit on the site. Most of the people on this site will be male and between 30-50 years old.

Industry/Entity Type

Auto Repair

Number of Pages Required

1 page

Colors

Designer to choose colors to be used in the design.

```html
<!DOCTYPE html>
<html lang="en">
<head>
<meta charset="utf-8">
<title>TorqueLane – Marketing for Auto Repair Shops</title>
<link href="https://fonts.googleapis.com/css2?family=Roboto+Condensed:wght@400;700&family=Roboto:wght@300;400;500;700&display=swap" rel="stylesheet">
<style>
:root{
  --pink:#f9285f;
  --pink-soft:#f9d5df;
  --ink:#333;
  --text:#555;
  --muted:#777;
  --light:#f2f2f2;
  --dark:#1d1d1f;
  --white:#fff;
}
*{box-sizing:border-box;margin:0;padding:0}
html,body{width:1200px;height:2418px;overflow:hidden}
body{position:relative;background:var(--white);font-family:'Roboto',sans-serif;color:var(--text)}
.abs{position:absolute}
.top-band{left:0;top:0;width:1200px;height:823px;background:var(--light)}
/* header */
.site-header{left:0;top:0;width:1200px;height:64px;background:var(--white);box-shadow:0 1px 3px rgba(0,0,0,.05)}
.logo{font-family:'Roboto Condensed',sans-serif;font-weight:700;color:var(--pink);font-size:23px;letter-spacing:-.3px}
.main-nav{left:328px;top:24px;font-family:'Roboto Condensed',sans-serif;font-size:12.5px;color:#444;display:flex;gap:9px}
.main-nav .active{color:var(--pink)}
.contact-item{font-family:'Roboto Condensed',sans-serif;font-size:10.5px;line-height:13px;color:#444}
.contact-item .hl{color:var(--pink)}
.login-btn{left:989px;top:14px;width:80px;height:35px;background:var(--pink);color:var(--white);font-family:'Roboto Condensed',sans-serif;font-size:12.5px;display:flex;align-items:center;justify-content:center;gap:6px}
.lang{left:1093px;top:16px;width:32px;height:32px;border:1px solid var(--pink);border-radius:50%;color:var(--pink);font-size:11px;display:flex;align-items:center;justify-content:center}
/* hero */
.hero{left:181px;top:64px;width:1019px;height:422px;background:linear-gradient(120deg,#1b1c22 0%,#2c3446 45%,#c9ccd3 80%,#e6e7ea 100%);border-bottom:5px solid var(--pink);border-bottom-left-radius:200px 120px;overflow:hidden}
.hero-copy{left:213px;top:156px;width:250px;color:var(--white)}
.hero-copy .hi{font-family:'Roboto Condensed',sans-serif;font-size:21px}
.hero-copy h1{font-family:'Roboto Condensed',sans-serif;font-weight:400;color:var(--pink);font-size:23px;margin:2px 0 10px;white-space:nowrap}
.hero-copy p{font-size:11px;line-height:18px;font-weight:300}
.hero-btn{left:213px;top:300px;width:164px;height:34px;background:var(--pink);color:var(--white);font-family:'Roboto Condensed',sans-serif;font-weight:700;font-size:12px;display:flex;align-items:center;justify-content:center;gap:6px}
.slide-dots{left:565px;top:475px;width:70px;height:20px;background:var(--white);border-radius:14px 14px 0 0;display:flex;justify-content:center;align-items:center;gap:4px}
.slide-dots i{width:6px;height:6px;border:1px solid var(--pink);border-radius:50%}
.slide-dots i.on{background:var(--pink)}
/* headings */
.sec-title{left:0;width:1200px;text-align:center;font-family:'Roboto Condensed',sans-serif;font-weight:700;color:var(--pink);font-size:27px}
.sec-sub{left:0;width:1200px;text-align:center;font-family:'Roboto Condensed',sans-serif;font-size:12px;color:#444}
.sec-sub b{color:var(--pink)}
/* feature cards */
.feature{top:588px;width:190px;height:199px;background:var(--white);text-align:center;padding-top:28px}
.feature h3{font-family:'Roboto Condensed',sans-serif;font-weight:700;color:var(--pink);font-size:18px;margin:10px 0 6px}
.feature p{font-size:11px;line-height:16px;color:var(--text);padding:0 28px}
/* about */
.about-photo{left:238px;top:874px;width:332px;height:260px;background:linear-gradient(135deg,#5d6468,#1f3b36 45%,#8b8f92 100%)}
.about-strip{left:184px;top:961px;width:54px;height:173px;background:var(--pink-soft)}
.about-strip span{position:absolute;left:33px;bottom:10px;transform-origin:left bottom;transform:rotate(-90deg);font-family:'Roboto Condensed',sans-serif;font-weight:700;font-size:12px;color:var(--pink);white-space:nowrap}
.about-tag{left:473px;top:1067px;width:97px;height:102px;background:var(--pink);color:var(--white);font-family:'Roboto Condensed',sans-serif;font-weight:700;font-size:13px;line-height:16px;padding:58px 0 0 10px}
.about-title{left:609px;top:866px;font-family:'Roboto Condensed',sans-serif;font-weight:700;color:var(--pink);font-size:27px}
.about-text{left:609px;top:912px;width:410px;font-size:11px;line-height:18px;color:var(--text)}
.about-text p+p{margin-top:8px}
.btn-outline{height:35px;border:1px solid #bbb;background:var(--white);font-family:'Roboto Condensed',sans-serif;font-size:12px;color:#444;display:flex;align-items:center;justify-content:center;gap:6px}
/* service posts */
.post{top:1316px;width:259px}
.post-photo{width:100%;height:200px}
.post-bar{position:relative;height:36px;background:var(--pink);color:var(--white);font-family:'Roboto Condensed',sans-serif;font-weight:700;font-size:13.5px;padding:10px 0 0 108px}
.post-icon{position:absolute;left:15px;top:-18px;width:80px;height:54px;background:var(--white);display:flex;align-items:center;justify-content:center}
.post p{font-size:11px;line-height:16.5px;color:var(--text);margin-top:27px;width:262px}
.circle-arrow{width:44px;height:44px;border:1.5px solid var(--pink);border-radius:50%;display:flex;align-items:center;justify-content:center}
/* team */
.tech-band{left:0;top:1762px;width:1200px;height:215px;background:linear-gradient(90deg,#1a1a1c,#2b2b2e 50%,#1a1a1c)}
.tech-title{left:0;top:1794px;width:1200px;text-align:center;color:var(--white);font-family:'Roboto',sans-serif;font-weight:700;font-size:26px;letter-spacing:-.5px}
.tech{top:1869px;width:187px}
.tech-photo{height:192px}
.tech-name{height:45px;background:var(--pink);color:var(--white);font-family:'Roboto Condensed',sans-serif;font-weight:700;font-size:13.5px;display:flex;align-items:center;justify-content:center}
/* footer */
.foot-col h4{font-family:'Roboto',sans-serif;font-weight:500;color:var(--pink);font-size:13px;margin-bottom:14px}
.foot-col li{list-style:none;font-size:10.5px;color:var(--muted);line-height:22.5px}
.foot-col li::before{content:"›";margin-right:5px}
.news{font-size:10.5px;color:var(--muted);line-height:12px;margin-bottom:16px}
.news .date{color:var(--pink);margin-top:3px;display:flex;align-items:center;gap:5px}
.find{font-size:10.5px;color:#555;display:flex;align-items:center;gap:7px;margin-bottom:10px}
.social{display:flex;gap:6px}
.social i{width:26px;height:26px;border:1.5px solid var(--pink);border-radius:50%;display:block}
.copyright{left:0;top:2380px;width:1200px;height:38px;background:var(--pink);color:var(--white);font-size:12px;display:flex;align-items:center;justify-content:center}
</style>
</head>
<body>
<div class="abs top-band"></div>

<header class="abs site-header">
  <div class="abs logo" style="left:86px;top:19px">TorqueLane</div>
  <nav class="abs main-nav">
    <span class="active">Home</span><span>I</span><span>Services</span><span>I</span><span>Review Software</span><span>I</span><span>Blog</span><span>I</span><span>Contact Us</span>
  </nav>
  <div class="abs contact-item" style="left:686px;top:18px;display:flex;gap:8px">
    <svg width="16" height="20" viewBox="0 0 16 20"><path d="M8 1a6 6 0 0 0-6 6c0 4.5 6 11 6 11s6-6.5 6-11a6 6 0 0 0-6-6z" fill="none" stroke="#f9285f" stroke-width="1.5"/><circle cx="8" cy="7" r="2.2" fill="none" stroke="#f9285f" stroke-width="1.5"/></svg>
    <div><span class="hl">No. 48 Piston Row,</span><br>Gearford, Australia.</div>
  </div>
  <div class="abs contact-item" style="left:836px;top:18px;display:flex;gap:8px">
    <svg width="20" height="18" viewBox="0 0 20 18"><path d="M2 12c5-4 11-4 16 0l-2 3-3-1v-2c-2-.6-4-.6-6 0v2l-3 1z" fill="none" stroke="#f9285f" stroke-width="1.4"/><path d="M11 2l4 4M15 2v4h-4" fill="none" stroke="#f9285f" stroke-width="1.4"/></svg>
    <div><span class="hl">00 555 010 204</span><br>hello@torquelane.test</div>
  </div>
  <div class="abs login-btn">
    <svg width="16" height="16" viewBox="0 0 16 16"><circle cx="8" cy="8" r="7" fill="none" stroke="#fff" stroke-width="1.2"/><path d="M4 8h7M8 5l3 3-3 3" fill="none" stroke="#fff" stroke-width="1.2"/></svg>SIGN UP
  </div>
  <div class="abs lang">EN</div>
</header>

<section>
  <div class="abs hero" role="img" aria-label="Mechanic in a blue cap and uniform fitting a car wheel with an impact wrench"></div>
  <div class="abs hero-copy">
    <div class="hi">Hi,</div>
    <h1>Fill Your Bays With New Drivers</h1>
    <p>We help auto repair shops get found online, earn more 5-star reviews and turn searches into booked jobs. Start with a free audit...</p>
  </div>
  <div class="abs hero-btn">Get My Free Visibility Audit <svg width="7" height="9" viewBox="0 0 7 9"><path d="M1 1l4 3.5L1 8" fill="none" stroke="#fff" stroke-width="1.6"/></svg></div>
  <div class="abs slide-dots"><i></i><i class="on"></i><i></i></div>
</section>

<section>
  <h2 class="abs sec-title" style="top:514px">How We Grow Your Shop</h2>
  <p class="abs sec-sub" style="top:551px">If Your Phone Isn't Ringing Enough ... We Get Auto Repair Shops Seen, Reviewed And Chosen By Local Drivers , <b>Start Now!!</b></p>

  <div class="abs feature" style="left:184px">
    <svg width="48" height="48" viewBox="0 0 48 48"><path d="M24 5l5.6 11.4 12.6 1.8-9.1 8.9 2.1 12.5L24 33.7l-11.2 5.9 2.1-12.5-9.1-8.9 12.6-1.8z" fill="none" stroke="#777" stroke-width="3" stroke-linejoin="round"/><path d="M24 13v15" stroke="#f9285f" stroke-width="3"/></svg>
    <h3>Review Software</h3><p>Collect 5-star reviews from every happy customer.</p>
  </div>
  <div class="abs feature" style="left:398px">
    <svg width="48" height="48" viewBox="0 0 48 48"><circle cx="20" cy="20" r="13" fill="none" stroke="#f9285f" stroke-width="4"/><path d="M30 30l12 12" stroke="#f9285f" stroke-width="5" stroke-linecap="round"/><path d="M14 24v-4M20 24v-8M26 24v-6" stroke="#f9285f" stroke-width="3"/></svg>
    <h3>Visibility Audit</h3><p>See exactly how drivers find your shop online.</p>
  </div>
  <div class="abs feature" style="left:612px">
    <svg width="48" height="48" viewBox="0 0 48 48"><path d="M24 4a12 12 0 0 0-12 12c0 9 12 22 12 22s12-13 12-22A12 12 0 0 0 24 4z" fill="#888"/><circle cx="24" cy="16" r="5" fill="#fff"/><ellipse cx="24" cy="42" rx="14" ry="3" fill="none" stroke="#f9285f" stroke-width="2"/></svg>
    <h3>Local SEO</h3><p>Rank higher when locals search for a mechanic.</p>
  </div>
  <div class="abs feature" style="left:826px">
    <svg width="56" height="48" viewBox="0 0 56 48"><rect x="4" y="6" width="48" height="32" rx="2" fill="none" stroke="#888" stroke-width="4"/><path d="M12 30l10-10 7 7 13-13" fill="none" stroke="#f9285f" stroke-width="3"/><path d="M20 44h16M28 38v6" stroke="#888" stroke-width="4"/></svg>
    <h3>Paid Ads</h3><p>Targeted ads that bring in real repair jobs.</p>
  </div>
</section>

<section>
  <div class="abs about-strip"><span>Best Agency of the Year</span></div>
  <div class="abs about-photo" role="img" aria-label="Smiling founder sitting against a dark green car in a parking garage"></div>
  <div class="abs about-tag">Dana Holt,<br>Founder</div>
  <h2 class="abs about-title">About Our Agency</h2>
  <div class="abs about-text">
    <p>Torque Lane Promotions is a digital marketing agency built only for the auto repair industry. We know how shop owners work, what customers search for and why a good review can matter more than a low price. Our team turns your reputation and online presence into a steady flow of booked appointments.</p>
    <p>Start with a free Visibility Audit to see where your shop stands, then let our Review Software gather honest feedback from every customer you serve, automatically.</p>
  </div>
  <div class="abs btn-outline" style="left:609px;top:1083px;width:90px">Read More <svg width="7" height="9" viewBox="0 0 7 9"><path d="M1 1l4 3.5L1 8" fill="none" stroke="#444" stroke-width="1.5"/></svg></div>
</section>

<section>
  <h2 class="abs sec-title" style="top:1242px">Alltime Best Services</h2>
  <p class="abs sec-sub" style="top:1281px">Marketing Tools Made for Repair Shops</p>

  <article class="abs post" style="left:184px">
    <div class="post-photo" role="img" aria-label="Blue rally car with open hood and exhaust smoke in a workshop" style="background:linear-gradient(135deg,#9aa3ad,#2a3a6a 50%,#d9dadc)"></div>
    <div class="post-bar"><div class="post-icon"><svg width="40" height="40" viewBox="0 0 40 40"><path d="M20 4l4.7 9.5 10.5 1.5-7.6 7.4 1.8 10.5L20 28l-9.4 4.9 1.8-10.5L4.8 15l10.5-1.5z" fill="none" stroke="#f9285f" stroke-width="2" stroke-linejoin="round"/></svg></div>Review Software</div>
    <p>Send review requests by text after every job, answer feedback in one place and show off your best ratings on search and maps.</p>
    <div class="btn-outline" style="margin-top:33px;width:90px">Sign Up <svg width="7" height="9" viewBox="0 0 7 9"><path d="M1 1l4 3.5L1 8" fill="none" stroke="#444" stroke-width="1.5"/></svg></div>
  </article>
  <article class="abs post" style="left:470px">
    <div class="post-photo" role="img" aria-label="Close view of a dark car's glowing red tail light" style="background:radial-gradient(circle at 55% 30%,#8a1a1a 0,#2a2a2e 30%,#101012 80%)"></div>
    <div class="post-bar"><div class="post-icon"><svg width="40" height="40" viewBox="0 0 40 40"><circle cx="17" cy="17" r="11" fill="none" stroke="#f9285f" stroke-width="2"/><path d="M25 25l10 10" stroke="#f9285f" stroke-width="3" stroke-linecap="round"/><path d="M12 21v-3M17 21v-7M22 21v-5" stroke="#f9285f" stroke-width="2"/></svg></div>Visibility Audit</div>
    <p>A free report on your listings, website speed, reviews and rankings against nearby shops, with clear next steps you can act on.</p>
    <div class="btn-outline" style="margin-top:33px;width:90px">Get Audit <svg width="7" height="9" viewBox="0 0 7 9"><path d="M1 1l4 3.5L1 8" fill="none" stroke="#444" stroke-width="1.5"/></svg></div>
  </article>
  <article class="abs post" style="left:757px">
    <div class="post-photo" role="img" aria-label="Mechanic in a bright garage working beside a racing car" style="background:linear-gradient(135deg,#e9eaec,#9da4ad 50%,#2b2f3a)"></div>
    <div class="post-bar"><div class="post-icon"><svg width="46" height="40" viewBox="0 0 46 40"><circle cx="23" cy="20" r="16" fill="none" stroke="#f9285f" stroke-width="3"/><circle cx="23" cy="20" r="10" fill="none" stroke="#f9285f" stroke-width="2"/><circle cx="23" cy="20" r="3" fill="#f9285f"/></svg></div>Paid Ad Campaigns</div>
    <p>Search and map ads aimed at drivers near your shop, tracked down to every call and booking so you know what each dollar returns.</p>
    <div class="btn-outline" style="margin-top:33px;width:90px">Read More <svg width="7" height="9" viewBox="0 0 7 9"><path d="M1 1l4 3.5L1 8" fill="none" stroke="#444" stroke-width="1.5"/></svg></div>
  </article>
  <div class="abs circle-arrow" style="left:162px;top:1412px"><svg width="10" height="14" viewBox="0 0 10 14"><path d="M8 1L2 7l6 6" fill="none" stroke="#f9285f" stroke-width="1.6"/></svg></div>
</section>

<section>
  <div class="abs tech-band" role="img" aria-label="Dark workshop backdrop"></div>
  <h2 class="abs tech-title">MEET OUR SPECIALISTS</h2>
  <div class="abs tech" style="left:184px"><div class="tech-photo" role="img" aria-label="Team member in a blue shirt with arms crossed" style="background:linear-gradient(160deg,#e8e8e8,#2f5fae 60%,#1d3f80)"></div><div class="tech-name">SEO Specialists</div></div>
  <div class="abs tech" style="left:400px"><div class="tech-photo" role="img" aria-label="Two team members reviewing a shop engine together" style="background:linear-gradient(160deg,#555,#d8dbe2 45%,#2b3f7a)"></div><div class="tech-name">Review Managers</div></div>
  <div class="abs tech" style="left:614px"><div class="tech-photo" role="img" aria-label="Team member beside a car wheel with a laptop nearby" style="background:linear-gradient(160deg,#444,#8e96a3 40%,#1f4ba0)"></div><div class="tech-name">Ad Strategists</div></div>
  <div class="abs tech" style="left:829px"><div class="tech-photo" role="img" aria-label="Team member in a cap leaning over an open engine bay" style="background:linear-gradient(160deg,#2a3c78,#c8ccd4 55%,#1b2b55)"></div><div class="tech-name">Web Designers</div></div>
  <div class="abs circle-arrow" style="left:997px;top:1966px;background:rgba(255,255,255,.05)"><svg width="10" height="14" viewBox="0 0 10 14"><path d="M2 1l6 6-6 6" fill="none" stroke="#f9285f" stroke-width="1.6"/></svg></div>
</section>

<footer>
  <div class="abs foot-col" style="left:184px;top:2205px;width:220px">
    <div class="logo" style="margin-bottom:8px">TorqueLane</div>
    <p style="font-size:10.5px;line-height:18px;color:var(--muted)">Marketing built only for mechanics. We help independent repair shops earn trust online, win more reviews and keep every bay busy, week after week.</p>
  </div>
  <div class="abs foot-col" style="left:445px;top:2207px">
    <h4>Our Services</h4>
    <ul><li>Review Software Sign Up</li><li>Free Visibility Audit</li><li>Local SEO for Repair Shops</li><li>Paid Search &amp; Map Ads</li><li>Shop Website Design &amp; Care</li></ul>
  </div>
  <div class="abs foot-col" style="left:654px;top:2207px;width:170px">
    <h4>Latest News</h4>
    <div class="news">How Reviews Bring More Cars Into Your Repair Bays<div class="date"><svg width="11" height="11" viewBox="0 0 11 11"><rect x="1" y="2" width="9" height="8" fill="none" stroke="#f9285f"/><path d="M1 4.5h9M3 1v2M8 1v2" stroke="#f9285f"/></svg>Aug 21, 2019</div></div>
    <div class="news">Five Quick Wins To Rank Your Shop Higher On Maps<div class="date"><svg width="11" height="11" viewBox="0 0 11 11"><rect x="1" y="2" width="9" height="8" fill="none" stroke="#f9285f"/><path d="M1 4.5h9M3 1v2M8 1v2" stroke="#f9285f"/></svg>Aug 21, 2019</div></div>
  </div>
  <div class="abs foot-col" style="left:863px;top:2207px">
    <h4>Find Us</h4>
    <div class="find"><svg width="20" height="20" viewBox="0 0 20 20"><circle cx="10" cy="10" r="9" fill="none" stroke="#777"/><path d="M6 5l2 0 1 3-1 1c1 2 2 3 3 3l1-1 3 1v2c-5 1-10-4-9-9z" fill="none" stroke="#777"/></svg>Phone: +00 5 5501 234</div>
    <div class="find"><svg width="20" height="20" viewBox="0 0 20 20"><circle cx="10" cy="10" r="9" fill="none" stroke="#777"/><rect x="5" y="6.5" width="10" height="7" fill="none" stroke="#777"/><path d="M5 6.5l5 4 5-4" fill="none" stroke="#777"/></svg>Email: info@torquelane.test</div>
    <div class="social"><i></i><i></i><i></i></div>
  </div>
  <div class="abs copyright">Copyright © 2019 Torque Lane Promotions. All rights reserved.</div>
</footer>
</body>
</html>
```